Lawn care business card

I am looking for a quality designed personal business card to represent the quality and elegant nature of our company. We separate ourselves in our market by the aesthetic value of our work, so I am looking for marketing material that does the same. We target our marketing high end customers, and we try to avoid price shoppers. I am open to all design options, so long as they are in line with our companies values.

We are tend to go with a retro look on everything from our logo and print material, to our uniforms. We like to portray and "old fashion" set of core values, with a modern elegance. So a wild and crazy look is out of the question.

Things I'd like on the card:
1.) Logo
2.) Phone number: (816) 555-0193
3.) Website: Verdanthollow.com
4.) Email: peterwalsh@verdanthollow.com
5.) My name: Peter Walsh
6.) Facebook link: facebook.com/VerdantHollowLawn
7.) Instagram: http://instagram.com/verdanthollow

Attached is a copy of our logo.

```html
<!DOCTYPE html>
<html lang="en">
<head>
<meta charset="utf-8">
<title>Verdant Hollow – Business Card</title>
<link rel="stylesheet" href="https://fonts.googleapis.com/css2?family=Lato:wght@400;700&display=swap">
<style>
  :root {
    --page-bg: #e9e6e1;
    --card-bg: #f7f7f4;
    --brand-orange: #ec5a24;
    --ink: #231f20;
    --band-black: #222222;
    --white: #ffffff;
  }
  * { margin: 0; padding: 0; box-sizing: border-box; }
  html, body {
    width: 1200px;
    height: 841px;
    overflow: hidden;
    background: var(--page-bg);
    font-family: "Lato", sans-serif;
  }
  .business-card {
    position: absolute;
    left: 100px;
    top: 135px;
    width: 1000px;
    height: 572px;
    background: var(--card-bg);
    overflow: hidden;
    box-shadow: 0 6px 24px rgba(0,0,0,0.12);
  }
  .card-swoosh {
    position: absolute;
    inset: 0;
    width: 100%;
    height: 100%;
  }
  .brand-mark {
    position: absolute;
    left: 70px;
    top: 78px;
    display: flex;
    align-items: center;
    gap: 22px;
  }
  .brand-dot {
    width: 96px;
    height: 96px;
    border-radius: 50%;
    background: var(--brand-orange);
  }
  .brand-name {
    font-weight: 700;
    font-size: 46px;
    color: var(--ink);
    letter-spacing: 1px;
  }
  .contact-block {
    position: absolute;
    right: 44px;
    top: 222px;
    text-align: right;
    color: var(--ink);
  }
  .contact-name {
    font-weight: 700;
    font-size: 44px;
    color: var(--brand-orange);
    text-transform: uppercase;
    letter-spacing: 0.5px;
    margin-bottom: 6px;
  }
  .contact-line {
    font-size: 24px;
    line-height: 34px;
  }
  .contact-label {
    color: var(--brand-orange);
    font-weight: 700;
  }
  .website {
    position: absolute;
    right: 44px;
    bottom: 24px;
    font-size: 30px;
    letter-spacing: 2px;
    color: var(--white);
  }
</style>
</head>
<body>
  <main class="business-card">
    <svg class="card-swoosh" viewBox="0 0 1000 572" preserveAspectRatio="none" aria-hidden="true">
      <path d="M0,398 C260,430 480,458 720,476 C480,466 250,444 0,418 Z" fill="var(--brand-orange)"/>
      <path d="M0,432 C300,462 650,488 1000,500 L1000,572 L0,572 Z" fill="var(--band-black)"/>
    </svg>

    <div class="brand-mark">
      <span class="brand-dot"></span>
      <span class="brand-name">Verdant Hollow</span>
    </div>

    <section class="contact-block">
      <h1 class="contact-name">Peter Walsh</h1>
      <p class="contact-line"><span class="contact-label">phone:</span> (816) 555-0193</p>
      <p class="contact-line"><span class="contact-label">email:</span> peterwalsh@verdanthollow.com</p>
      <p class="contact-line"><span class="contact-label">Instagram:</span> http://instagram.com/verdanthollow</p>
      <p class="contact-line"><span class="contact-label">Facebook:</span> facebook.com/VerdantHollowLawn</p>
    </section>

    <p class="website">www.Verdanthollow.com</p>
  </main>
</body>
</html>
```